Velvette by Monica Darsh business cards

I am after a business card that will fit the name of my business - velvette.
I want something classy and sexy and nothing tacky.
Ideas that I like are Zebra print backgrounds glitter back grounds
Two ideas I had were
1. Zebra print in black and white, the name Velvette by Monica Darsh and a shilouette of a woman laying on top of the name. Or instead of zebra a glitter background.
2. Idea very similar except for instead of a woman a pair of lips maybe a hot pink glitter or a gold glitter depending on background with the business name between the lips.
Or you can do something completely different.

Industry/Entity Type

Business

```html
<!DOCTYPE html>
<html lang="en">
<head>
<meta charset="utf-8">
<title>Velvette by Monica Darsh – Business Card</title>
<link rel="stylesheet" href="https://fonts.googleapis.com/css2?family=Damion&family=Dancing+Script:wght@400;700&family=Josefin+Sans:wght@300&family=Montserrat:wght@800&display=swap">
<style>
  :root {
    --page: #ffffff;
    --glitter-light: #f07a94;
    --glitter-mid: #d9445f;
    --glitter-deep: #b0203a;
    --lips-light: #e8232e;
    --lips-deep: #a80f1a;
    --script-coral: #f7837a;
    --glow: rgba(255, 236, 220, 0.95);
    --ivory: #f7f2ee;
    --aqua-light: #effafa;
    --aqua-mid: #dcf1f2;
    --contact-red: #ef4b4b;
    --label-ink: #111111;
  }
  * { margin: 0; padding: 0; box-sizing: border-box; }
  html, body { width: 800px; height: 1200px; overflow: hidden; background: var(--page); }
  .canvas { position: relative; width: 800px; height: 1200px; }

  .glitter {
    background: radial-gradient(circle at 30% 35%, var(--glitter-light), var(--glitter-mid) 55%, var(--glitter-deep));
  }

  .card { position: absolute; width: 425px; height: 236px; overflow: hidden; }
  .card--front { left: 202px; top: 32px; }
  .card--back { left: 200px; top: 369px; display: flex; }

  .side-label {
    position: absolute; width: 800px; left: 0; text-align: center;
    font-family: "Montserrat", sans-serif; font-weight: 800; font-size: 28px;
    letter-spacing: 3px; color: var(--label-ink);
  }
  .side-label--front { top: 285px; }
  .side-label--back { top: 624px; }

  .lips-art { position: absolute; left: 38px; top: 12px; width: 352px; height: 218px; }

  .wordmark {
    font-family: "Damion", cursive; color: var(--script-coral);
    text-shadow: 0 0 6px var(--glow), 0 0 14px var(--glow);
  }
  .tagline {
    font-family: "Josefin Sans", sans-serif; font-weight: 300;
    color: var(--ivory); text-transform: uppercase;
  }
  .card--front .wordmark {
    position: absolute; left: 0; right: 0; top: 70px; text-align: center;
    font-size: 66px; line-height: 1;
  }
  .card--front .tagline {
    position: absolute; left: 0; right: 0; top: 170px; text-align: center;
    font-size: 30px; letter-spacing: 3px;
  }

  .back-strip { position: relative; width: 128px; height: 236px; flex: none; }
  .back-strip__rotated {
    position: absolute; width: 236px; height: 128px; left: -54px; top: 54px;
    transform: rotate(-90deg); text-align: center;
  }
  .back-strip .wordmark { display: block; font-size: 46px; line-height: 1; margin-top: 30px; }
  .back-strip .tagline { display: block; font-size: 17px; letter-spacing: 1.5px; margin-top: 6px; }

  .back-panel {
    position: relative; width: 297px; height: 236px;
    background: linear-gradient(135deg, var(--aqua-light), var(--aqua-mid));
  }
  .back-panel__rotated {
    position: absolute; width: 236px; height: 297px; left: 30.5px; top: -30.5px;
    transform: rotate(-90deg);
  }
  .contact-list {
    position: absolute; left: 0; top: 10px; width: 236px; text-align: center;
    font-family: "Dancing Script", cursive; color: var(--contact-red);
  }
  .contact-list dt { font-weight: 700; font-size: 17px; line-height: 26px; }
  .contact-list dd { font-weight: 400; font-size: 20px; line-height: 30px; }
  .contact-list dd.contact-list__small { font-size: 17px; }

  .brand-mark {
    position: absolute; left: 148px; top: 240px; display: flex; align-items: center; gap: 5px;
    font-family: "Dancing Script", cursive; font-weight: 700; font-size: 18px; color: var(--contact-red);
  }
  .brand-mark__dot { width: 12px; height: 12px; border-radius: 50%; background: var(--contact-red); }
</style>
</head>
<body>
<main class="canvas">
  <section class="card card--front glitter" aria-label="Card front">
    <svg class="lips-art" viewBox="0 0 352 218" role="img" aria-label="Red glitter lips illustration">
      <defs>
        <radialGradient id="lipsFill" cx="50%" cy="45%" r="60%">
          <stop offset="0" stop-color="var(--lips-light)"/>
          <stop offset="1" stop-color="var(--lips-deep)"/>
        </radialGradient>
      </defs>
      <ellipse cx="176" cy="109" rx="174" ry="106" fill="url(#lipsFill)"/>
    </svg>
    <h1 class="wordmark">Velvette</h1>
    <p class="tagline">by Monica Darsh</p>
  </section>
  <p class="side-label side-label--front">FRONT</p>

  <section class="card card--back" aria-label="Card back">
    <div class="back-strip glitter">
      <div class="back-strip__rotated">
        <span class="wordmark">Velvette</span>
        <span class="tagline">by Monica Darsh</span>
      </div>
    </div>
    <div class="back-panel">
      <div class="back-panel__rotated">
        <dl class="contact-list">
          <dt>phone</dt>
          <dd>000-000-00-00</dd>
          <dt>mobile</dt>
          <dd>000-000-00-00</dd>
          <dt>address</dt>
          <dd class="contact-list__small">Main Street, Australia</dd>
          <dt>website</dt>
          <dd class="contact-list__small">www.velvette.com</dd>
        </dl>
        <div class="brand-mark"><span class="brand-mark__dot"></span>Velvette</div>
      </div>
    </div>
  </section>
  <p class="side-label side-label--back">BACK</p>
</main>
</body>
</html>
```